We are in search of a new business card design for our business. We have a Mexican Grocery Store called Tortilla Grove Market, we would like to see that some have mexican design, but we are open to any type of designs.

Phone: to be announced
Fax: to be announced

Address is:
2415 Calloway Blvd
Rosewell, MD 21390

```html
<!DOCTYPE html>
<html lang="en">
<head>
<meta charset="UTF-8">
<title>Tortilla Grove Market – Business Card</title>
<link rel="stylesheet" href="https://fonts.googleapis.com/css2?family=Montserrat:wght@700&family=Questrial&display=swap">
<style>
  :root {
    --chili-red: #b8252f;
    --sun-yellow: #fde21a;
    --card-white: #fefef9;
    --leaf-green: #1f6b38;
    --ink-grey: #4a4a4a;
    --label-red: #a3181f;
  }
  html, body {
    margin: 0;
    padding: 0;
    width: 1200px;
    height: 720px;
    overflow: hidden;
    background: #ffffff;
  }
  .card {
    position: relative;
    width: 1200px;
    height: 720px;
    overflow: hidden;
    font-family: "Questrial", sans-serif;
  }
  .card-pattern {
    position: absolute;
    inset: 0;
    background:
      radial-gradient(ellipse at 50% 50%, var(--chili-red) 40%, transparent 75%),
      linear-gradient(135deg, var(--chili-red) 0%, #d9552a 30%, var(--sun-yellow) 55%, #d24a2b 75%, var(--chili-red) 100%);
  }
  .card-panel {
    position: absolute;
    left: 69px;
    top: 69px;
    width: 1062px;
    height: 582px;
    background: var(--card-white);
  }
  .brand-name {
    position: absolute;
    left: 110px;
    top: 308px;
    width: 390px;
    margin: 0;
    text-align: center;
    font-family: "Montserrat", sans-serif;
    font-weight: 700;
    font-size: 44px;
    line-height: 1.15;
    color: var(--label-red);
  }
  .contact {
    position: absolute;
    left: 656px;
    top: 166px;
    color: var(--ink-grey);
  }
  .person-name {
    margin: 0;
    font-family: "Montserrat", sans-serif;
    font-weight: 700;
    font-size: 37px;
    line-height: 44px;
    color: var(--leaf-green);
  }
  .person-role {
    margin: 0;
    font-size: 28px;
    line-height: 34px;
  }
  .address {
    margin: 58px 0 0;
    font-style: normal;
    font-size: 28px;
    line-height: 38px;
  }
  .lines {
    margin: 52px 0 0;
    font-size: 28px;
    line-height: 38px;
  }
  .lines p { margin: 0; }
  .lines .label {
    font-family: "Montserrat", sans-serif;
    font-weight: 700;
    font-size: 26px;
    color: var(--label-red);
  }
  .lines .email-value { font-size: 23px; }
</style>
</head>
<body>
  <div class="card">
    <div class="card-pattern" role="img" aria-label="Red and yellow shattered abstract pattern background"></div>
    <div class="card-panel"></div>

    <p class="brand-name">Tortilla Grove Market</p>

    <div class="contact">
      <h1 class="person-name">YOUR NAME</h1>
      <p class="person-role">Designation Here</p>
      <address class="address">2415 Calloway Blvd<br>Rosewell, MD 21390</address>
      <div class="lines">
        <p><span class="label">Phone:</span> 12 34 56 78</p>
        <p><span class="label">Fax:</span> 12 34 56 78</p>
        <p><span class="label">Email:</span>&nbsp; <span class="email-value">hello@tortillagrove.com</span></p>
      </div>
    </div>
  </div>
</body>
</html>
```